Plakat-Design für Chor und Blasorchester
Zielgruppe
Konzert eines Orchesters zusammen mit drei Chören.
Zielgruppe Musikinteressierte allen Alters
(Alter der Musiker/Sänger 15-85)
Aufgabenstellung
PLakat wird in erster Linie in A3 und A4 gedruck.
Vermutlich machen wir auch Flyer

```html
<!DOCTYPE html>
<html lang="de">
<head>
<meta charset="utf-8">
<title>Ohrwürmer – Konzertplakat</title>
<link rel="stylesheet" href="https://fonts.googleapis.com/css2?family=Source+Sans+3:wght@400;600;700;800&display=swap">
<style>
  :root {
    --gold: #f0c91f;
    --gold-deep: #e8b81c;
    --olive-gold: #9c8414;
    --olive-text: #7a6a14;
    --white: #ffffff;
    --grey-light: #d6d6dc;
    --lavender: #a9acd8;
    --direction: #eceef8;
    --footer: #d3d1c2;
    --green-dark: #2b392c;
    --blue: #233a7a;
    --blue-deep: #171d48;
    --yellow: #d8b92a;
  }
  html, body { margin: 0; padding: 0; overflow: hidden; }
  body { width: 853px; height: 1200px; background: var(--green-dark); }
  .poster {
    position: relative; width: 853px; height: 1200px; overflow: hidden;
    font-family: "Source Sans 3", sans-serif;
  }
  .layer { position: absolute; left: 0; top: 0; }
  .clef-area { position: absolute; left: 40px; top: 715px; }
  .type text { font-family: "Source Sans 3", sans-serif; }
  .title { font-size: 150px; font-weight: 800; fill: var(--white); }
  .title .accent { fill: var(--gold); }
  .subtitle { font-size: 70px; font-weight: 700; fill: var(--white); }
  .subtitle .accent { fill: var(--olive-gold); }
  .tagline { font-size: 36px; font-weight: 700; fill: var(--grey-light); }
  .tagline .accent { fill: var(--olive-text); }
  .ensemble { font-size: 26px; font-weight: 600; fill: var(--lavender); }
  .direction { font-size: 30px; font-weight: 700; fill: var(--direction); }
  .event-date { font-size: 44px; font-weight: 700; fill: var(--gold-deep); }
  .event-venue { font-size: 35px; font-weight: 700; fill: var(--white); }
  .admission { font-size: 25px; font-weight: 400; fill: var(--footer); }
</style>
</head>
<body>
<div class="poster">
  <svg class="layer backdrop" width="853" height="1200" viewBox="0 0 853 1200" aria-hidden="true">
    <defs>
      <linearGradient id="yellowFade" x1="0" y1="0" x2="1" y2="0">
        <stop offset="0" stop-color="#d8b92a"/>
        <stop offset="0.22" stop-color="#d2b42a"/>
        <stop offset="0.38" stop-color="#3a4330"/>
        <stop offset="1" stop-color="#2b392c"/>
      </linearGradient>
      <linearGradient id="oliveBand" x1="0" y1="0" x2="1" y2="1">
        <stop offset="0" stop-color="#4a5236"/>
        <stop offset="0.5" stop-color="#1f271b"/>
        <stop offset="1" stop-color="#1b2218"/>
      </linearGradient>
      <linearGradient id="blueFall" x1="0" y1="0" x2="0" y2="1">
        <stop offset="0" stop-color="#26406f"/>
        <stop offset="0.55" stop-color="#233a7a"/>
        <stop offset="1" stop-color="#171d48"/>
      </linearGradient>
    </defs>
    <rect width="853" height="1200" fill="#2b392c"/>
    <path d="M0 200 C200 420 520 480 853 360 L853 900 C600 880 300 700 0 340 Z" fill="url(#oliveBand)"/>
    <path d="M0 340 C250 650 550 860 853 895 L853 1200 L0 1200 Z" fill="url(#yellowFade)"/>
    <path d="M248 0 L853 0 L853 893 C690 880 540 850 412 795 Z" fill="url(#blueFall)"/>
    <path d="M0 0 L853 0 L853 355 C600 470 320 430 0 200 Z" fill="rgba(10,18,30,0.28)"/>
  </svg>

  <svg class="clef-area" width="190" height="470" role="img" aria-label="Violinschlüssel als zurückhaltendes Prägemotiv">
    <defs>
      <radialGradient id="clefTone" cx="0.5" cy="0.5" r="0.5">
        <stop offset="0" stop-color="#e2c23a" stop-opacity="0.35"/>
        <stop offset="1" stop-color="#d8b92a" stop-opacity="0"/>
      </radialGradient>
    </defs>
    <ellipse cx="95" cy="235" rx="95" ry="235" fill="url(#clefTone)"/>
  </svg>

  <svg class="layer type" width="853" height="1200" viewBox="0 0 853 1200">
    <defs>
      <filter id="lift" x="-10%" y="-30%" width="120%" height="160%">
        <feDropShadow dx="0" dy="3" stdDeviation="3" flood-color="#000" flood-opacity="0.35"/>
      </filter>
    </defs>
    <g class="title-block" filter="url(#lift)">
      <text class="title" x="50" y="241" textLength="720" lengthAdjust="spacingAndGlyphs" transform="rotate(-5.4 50 241)"><tspan class="accent">Ohr</tspan>würmer</text>
      <text class="subtitle" x="207" y="302" textLength="607" lengthAdjust="spacingAndGlyphs" transform="rotate(-5.4 207 302)"><tspan class="accent">von</tspan> Verdano bis Corwen</text>
      <text class="tagline" x="218" y="344" textLength="599" lengthAdjust="spacingAndGlyphs" transform="rotate(-5.4 218 344)"><tspan class="accent">für Cho</tspan>r und sinfonisches Blasorchester</text>
    </g>

    <g class="ensembles" text-anchor="end">
      <text class="ensemble" x="822" y="523">Vivace Chor Seehafen (D)</text>
      <text class="ensemble" x="822" y="554">Gemischter Chor Tannfeld (Ch)</text>
      <text class="ensemble" x="822" y="585">Chorwerk Eschwil-Bachmatt (Ch)</text>
      <text class="ensemble" x="822" y="616">Musikverein Riedhausen (D)</text>
    </g>

    <g class="direction-block" text-anchor="end">
      <text class="direction" x="818" y="690">Leitung:  Marlene Sonnberger</text>
      <text class="direction" x="816" y="725">Georg Tanner</text>
    </g>

    <g class="dates" filter="url(#lift)">
      <text class="event-date" x="282" y="937">19. NOV 2017, 17:00 Uhr</text>
      <text class="event-venue" x="281" y="981">Kirche St. Lorenz Seehafen</text>
      <text class="event-date" x="283" y="1055">26. NOV 2017, 17:00 Uhr</text>
      <text class="event-venue" x="283" y="1097">Markus – Kirche Eschwil</text>
    </g>

    <text class="admission" x="283" y="1170">Eintritt Frei – Spende freundlich erbeten</text>
  </svg>
</div>
</body>
</html>
```